Essential oil label for bottles

Looking to modify our current logo and label design. It looks too simple. I will attach images of our competitors to use as examples. Our company name is Velnora. We have 2 different bottles. Clear and amber color. Going forward, we will be using only the amber bottle. The other 2 images are the biggest sellers brands. We want to make some adjustments to ours.

Target Market(s)

Brindex sales

Industry/Entity Type

Essential oil, perfume

Colors

Designer to choose only greyscale colors for use in the design.

Requirements
Nice to have
• A slight change to fonts and logo design. Maybe change the font and design of the word "Velnora" in our logo. Maybe add something to the label to make it stand out more but still keeping it clean and modern
Should not have
• No colors, besides, black, grays, whites, and off white.

```html
<!DOCTYPE html>
<html lang="en">
<head>
<meta charset="utf-8">
<title>Velnora Fragrance Oil Label</title>
<link rel="stylesheet" href="https://fonts.googleapis.com/css2?family=Poppins:wght@300;400;500&display=swap">
<style>
  :root {
    --page: #ffffff;
    --label: #050505;
    --label-edge: #1c1c1c;
    --ink: #ffffff;
    --ink-soft: #e6e6e6;
  }
  * { margin: 0; padding: 0; box-sizing: border-box; }
  html, body {
    width: 1200px;
    height: 1013px;
    overflow: hidden;
    background: var(--page);
    font-family: "Poppins", sans-serif;
  }
  .canvas {
    position: relative;
    width: 1200px;
    height: 1013px;
  }
  .label {
    position: absolute;
    left: 359px;
    top: 166px;
    width: 482px;
    height: 680px;
    background: linear-gradient(90deg, var(--label-edge) 0%, var(--label) 18%, var(--label) 100%);
    color: var(--ink);
    text-align: center;
  }
  .label > * {
    position: absolute;
    left: 0;
    right: 0;
  }
  .brand-name {
    top: 140px;
    font-size: 22px;
    font-weight: 400;
    letter-spacing: 0.32em;
    padding-left: 0.32em;
  }
  .brand-rule {
    top: 229px;
    left: 208px;
    right: auto;
    width: 66px;
    height: 3px;
    background: var(--ink);
  }
  .product-name {
    top: 300px;
    font-size: 62px;
    font-weight: 500;
    line-height: 1;
    letter-spacing: 0.02em;
  }
  .product-type {
    top: 432px;
    font-size: 26px;
    font-weight: 500;
    letter-spacing: 0.06em;
  }
  .divider {
    top: 473px;
    display: flex;
    align-items: center;
    justify-content: center;
    gap: 10px;
  }
  .divider .line {
    width: 106px;
    height: 1px;
    background: var(--ink-soft);
  }
  .divider .diamond {
    width: 10px;
    height: 10px;
    background: var(--ink);
    transform: rotate(45deg);
  }
  .notes {
    top: 500px;
    list-style: none;
    font-size: 15px;
    font-weight: 300;
    line-height: 25.5px;
    color: var(--ink-soft);
  }
  .volume {
    top: 634px;
    font-size: 16px;
    font-weight: 400;
    letter-spacing: 0.04em;
  }
</style>
</head>
<body>
  <main class="canvas">
    <section class="label">
      <div class="brand-name">VELNORA</div>
      <div class="brand-rule"></div>
      <h1 class="product-name">OWN PATH</h1>
      <h2 class="product-type">FRAGRANCE OIL</h2>
      <div class="divider"><span class="line"></span><span class="diamond"></span><span class="line"></span></div>
      <ul class="notes">
        <li>OUD WOOD</li>
        <li>LEATHER</li>
        <li>SANDALWOOD</li>
      </ul>
      <div class="volume">200 ML</div>
    </section>
  </main>
</body>
</html>
```